Business card for Bio pharmaceutical company

Hello,
We are a bio pharmaceutical contract manufacturing company in Brisbane, Australia. Can you please create a new business card design. Please go to our website for colours http://www.veltromedix.com.au.
On the back can you include the cartoon mascot Tobi Warn and the tagline
"A Global Biopharmaceutical Contract Development Manufacturing Company"
Target Market(s)
Biotechnology
Industry/Entity Type
Pharmaceutical
Contact Information for Business Card
Karen Holbrooke
Business Development Manager
karen.holbrooke@veltromedix.com.au
1937 Mulgrave Street Kelby Queesnland 4076 Australia
T: +61 7 3591 6042
M +61 427 516 908
F +61 7 3648 2095
www.veltromedix.com.au

```html
<!DOCTYPE html>
<html lang="en">
<head>
<meta charset="utf-8">
<title>VeltroMedix Business Card</title>
<link rel="stylesheet" href="https://fonts.googleapis.com/css2?family=Exo+2:wght@400;500;700&display=swap">
<style>
  :root {
    --page-bg: #c9ccd1;
    --card-white: #ffffff;
    --card-grey: #e6e7e8;
    --brand-blue: #0b4f74;
    --brand-lime: #b8cf3c;
    --text-dark: #3b3b3b;
    --text-light: #ffffff;
  }
  * { margin: 0; padding: 0; box-sizing: border-box; }
  html, body { width: 1200px; height: 866px; overflow: hidden; }
  body {
    background: var(--page-bg);
    font-family: "Exo 2", Arial, sans-serif;
    position: relative;
  }
  .card {
    position: absolute;
    width: 540px;
    height: 310px;
    top: 278px;
    overflow: hidden;
    background: radial-gradient(ellipse at 45% 45%, var(--card-white) 0%, var(--card-grey) 100%);
    box-shadow: 0 6px 18px rgba(0,0,0,0.18);
  }
  .card--back { left: 40px; }
  .card--front { left: 620px; }

  .brand {
    position: absolute;
    display: flex;
    align-items: center;
    gap: 10px;
  }
  .brand__name {
    color: var(--brand-blue);
    font-weight: 700;
    letter-spacing: 0.5px;
  }
  .brand__mark { background: var(--brand-lime); }
  .card--back .brand {
    left: 0; right: 0; top: 0; bottom: 0;
    justify-content: center;
  }
  .card--back .brand__name { font-size: 46px; }
  .card--back .brand__mark { width: 30px; height: 30px; }

  .card--front .brand { left: 34px; top: 104px; }
  .card--front .brand__name { font-size: 32px; }
  .card--front .brand__mark { width: 18px; height: 18px; }

  .card__shape { position: absolute; inset: 0; }

  .holder {
    position: absolute;
    right: 30px;
    top: 18px;
    text-align: right;
    color: var(--text-dark);
  }
  .holder__name { font-size: 17px; font-weight: 500; letter-spacing: 1px; }
  .holder__title { font-size: 12px; margin-top: 2px; }

  .address {
    position: absolute;
    right: 30px;
    top: 136px;
    text-align: right;
    color: var(--text-light);
    font-size: 11.5px;
    line-height: 1.45;
  }
  .website {
    position: absolute;
    right: 30px;
    top: 200px;
    color: var(--text-light);
    font-size: 11.5px;
  }
  .contacts {
    position: absolute;
    left: 40px;
    bottom: 16px;
    list-style: none;
    color: var(--text-light);
    font-size: 10.5px;
  }
  .contacts li {
    display: flex;
    align-items: center;
    gap: 8px;
    height: 17px;
  }
  .contacts svg { width: 11px; height: 11px; fill: var(--text-light); }
</style>
</head>
<body>

  <section class="card card--back">
    <div class="brand">
      <span class="brand__name">VeltroMedix</span>
      <span class="brand__mark"></span>
    </div>
  </section>

  <section class="card card--front">
    <svg class="card__shape" viewBox="0 0 540 310" preserveAspectRatio="none">
      <path d="M0 188 C250 176 400 126 525 76 C400 138 260 190 0 205 Z" fill="var(--brand-lime)"/>
      <path d="M0 207 C260 194 400 142 540 80 L540 310 L0 310 Z" fill="var(--brand-blue)"/>
    </svg>

    <div class="brand">
      <span class="brand__name">VeltroMedix</span>
      <span class="brand__mark"></span>
    </div>

    <div class="holder">
      <div class="holder__name">MARCUS HOLLAND</div>
      <div class="holder__title">Managing Director</div>
    </div>

    <div class="address">047.12th floor,Park<br>Crescent Road KLV</div>
    <div class="website">www.yoursitename.com</div>

    <ul class="contacts">
      <li>
        <svg viewBox="0 0 24 24"><path d="M6.6 10.8a15 15 0 0 0 6.6 6.6l2.2-2.2a1 1 0 0 1 1-.25 11.4 11.4 0 0 0 3.6.57 1 1 0 0 1 1 1V20a1 1 0 0 1-1 1A17 17 0 0 1 3 4a1 1 0 0 1 1-1h3.5a1 1 0 0 1 1 1c0 1.25.2 2.45.57 3.57a1 1 0 0 1-.25 1z"/></svg>
        <span>013 456 7890</span>
      </li>
      <li>
        <svg viewBox="0 0 24 24"><path d="M7 1h10a2 2 0 0 1 2 2v18a2 2 0 0 1-2 2H7a2 2 0 0 1-2-2V3a2 2 0 0 1 2-2zm0 3v14h10V4zm5 15.5a1 1 0 1 0 0 2 1 1 0 0 0 0-2z"/></svg>
        <span>013 456 7890</span>
      </li>
      <li>
        <svg viewBox="0 0 24 24"><path d="M6 2h10l2 2v5h2a2 2 0 0 1 2 2v9a2 2 0 0 1-2 2H4a2 2 0 0 1-2-2v-9a2 2 0 0 1 2-2h2zm2 2v5h8V5l-1-1zm8 10H8v2h8z"/></svg>
        <span>013 456 7890</span>
      </li>
      <li>
        <svg viewBox="0 0 24 24"><path d="M2 5h20v14H2zm2 2v.5l8 5 8-5V7zm0 2.8V17h16V9.8l-8 5z"/></svg>
        <span>yourname@mail.com</span>
      </li>
    </ul>
  </section>

</body>
</html>
```